KEV.PRO- Darren Holcombe Fitness- needs a clever business card using the logo, name, info, contact

I need a business card designed for my Online Personal Training company called KEV.PRO, abbreviation for Darren Holcombe Fitness. My company focuses on coaching in personal health and personal growth to unleash your greatest potential. I would like to see designs that use my color scheme of a redish-orange (C:0,M:84,Y:100,K:0), grey, white, black, and my company font is OSWALD. The final design should communicate some aspects of design, health, motivation, growth, in some way. The logo is very important to the company and can be displayed in any of the colors previously mentioned. Must include the company name, my website: www.kev-pro.example , my email: dan@kev-pro.example

Target Market(s)

Personal health, fitness, general public, those who lack knowledge, awareness, and confidence in personal health

Industry/Entity Type

Personal Trainer

Font styles to use
Other font styles liked:
• OSWALD. (Bold, Regular, Light)

Colors
f37122
ffffff
9d9d9d
000000

Requirements
Must have
• Must include the logo, company name, my website: www.kev-pro.example , my email: dan@kev-pro.example
Nice to have
• Variations of the colors scheme of a redish-orange (C:0,M:84,Y:100,K:0), grey, white, black. Logo, card, or text can be in any of these colors.
• Possible quote like "Take control of your personal health to unleash your greatest potential" or "Unleashing your greatness first begins with fitness of the body and mind"

```html
<!DOCTYPE html>
<html lang="en">
<head>
<meta charset="utf-8">
<title>KEV.PRO Business Card</title>
<link rel="stylesheet" href="https://fonts.googleapis.com/css2?family=Oswald:wght@300;400;700&display=swap">
<style>
  :root {
    --brand-orange: #f15a24;
    --ink: #222222;
    --ink-soft: #333333;
    --grey: #9d9d9d;
    --white: #ffffff;
    --stage: #e9e7e4;
    --card-dark-1: #2c2c2c;
    --card-dark-2: #0f0f0f;
  }
  * { margin: 0; padding: 0; box-sizing: border-box; }
  html, body {
    width: 900px; height: 1200px; overflow: hidden;
    background: var(--stage);
    font-family: "Oswald", sans-serif;
  }
  .stage { position: relative; width: 900px; height: 1200px; }
  .card {
    position: absolute; left: 82px; width: 733px; height: 428px;
    border-radius: 22px; overflow: hidden;
  }
  .card--front { top: 137px; background: var(--white); }
  .card--back {
    top: 633px;
    background: linear-gradient(100deg, var(--card-dark-1) 0%, var(--card-dark-2) 100%);
  }
  .brand-mark {
    position: absolute; display: flex; align-items: center; gap: 14px;
  }
  .brand-mark__dot {
    width: 34px; height: 34px; border-radius: 50%;
    background: var(--brand-orange); flex: none;
  }
  .brand-mark__name {
    font-weight: 700; font-size: 54px; line-height: 1;
    color: var(--brand-orange); letter-spacing: 0.5px;
  }
  .card--front .brand-mark { left: 118px; top: 186px; }
  .card--back .brand-mark { left: 88px; top: 152px; }
  .divider { position: absolute; width: 2px; }
  .card--front .divider { left: 377px; top: 143px; height: 140px; background: var(--ink-soft); }
  .card--back .divider { left: 349px; top: 139px; height: 150px; background: #cfcfcf; }
  .identity { position: absolute; left: 406px; top: 136px; }
  .identity__name {
    font-weight: 700; font-size: 58px; line-height: 1; color: var(--ink);
  }
  .identity__tagline {
    font-weight: 300; font-size: 17.5px; line-height: 1.1; color: var(--ink-soft);
    padding-bottom: 6px; border-bottom: 3px solid var(--brand-orange);
    width: 196px; white-space: nowrap;
  }
  .contact { margin-top: 8px; }
  .contact__line {
    font-weight: 400; font-size: 17px; line-height: 24px;
    color: var(--brand-orange); white-space: nowrap;
  }
  .back-identity {
    position: absolute; left: 0; width: 268px; top: 272px; text-align: center;
    padding-left: 22px;
  }
  .back-identity__name {
    font-weight: 700; font-size: 38px; line-height: 1; color: var(--white);
  }
  .back-identity__tagline {
    font-weight: 300; font-size: 12px; color: #bdbdbd; white-space: nowrap;
  }
  .motto {
    position: absolute; right: 49px; top: 132px; text-align: right;
    font-weight: 400; font-size: 29px; line-height: 42.5px; color: var(--white);
  }
</style>
</head>
<body>
<main class="stage">
  <section class="card card--front" aria-label="Business card front">
    <div class="brand-mark">
      <span class="brand-mark__dot"></span>
      <span class="brand-mark__name">KEV.PRO</span>
    </div>
    <span class="divider"></span>
    <div class="identity">
      <h1 class="identity__name">KEV.PRO</h1>
      <p class="identity__tagline">DARREN HOLCOMBE.FITNESS</p>
      <div class="contact">
        <p class="contact__line">WWW.KEV-PRO.EXAMPLE</p>
        <p class="contact__line">EMAIL: DAN@KEV-PRO.EXAMPLE</p>
      </div>
    </div>
  </section>

  <section class="card card--back" aria-label="Business card back">
    <div class="brand-mark">
      <span class="brand-mark__dot"></span>
      <span class="brand-mark__name">KEV.PRO</span>
    </div>
    <div class="back-identity">
      <p class="back-identity__name">KEV.PRO</p>
      <p class="back-identity__tagline">DARREN HOLCOMBE.FITNESS</p>
    </div>
    <span class="divider"></span>
    <p class="motto">TAKE CONTROL OF<br>YOUR PERSONAL HEALTH<br>TO UNLEASH YOUR<br>GREATEST POTENTIAL</p>
  </section>
</main>
</body>
</html>
```